The Pixel Tavern Business card.

A Simple card with our Logo and contact information. To give to investors and other professionals.

We are a nerd themed bar.
our target market is young professionals age 21+ but the real purpose of this business card is to present to potential investors and other professionals with our contact information. as we are still looking for funding before we start up.

I am partial to green and my partner likes red we are open to iteration.

Target Market(s)

Investors

Industry/Entity Type

Business

Contact Information for Business Card

Marcus Henley (555) 730-6621 kent.w4100@mailbox-demo.net Brian Tolle (555) 918-2047 briant731@mailbox-demo.net

Font styles to use
Serif

Requirements
Nice to have
• Keep it simple but not boring.
• Use the Logos but feel free to edit them to match theme/colors.
• Keep the back clean and use one of the Logos.

```html
<!DOCTYPE html>
<html lang="en">
<head>
<meta charset="utf-8">
<title>The Pixel Tavern — Business Card</title>
<link href="https://fonts.googleapis.com/css2?family=Open+Sans:wght@400;700&family=Libre+Baskerville&display=swap" rel="stylesheet">
<style>
  :root {
    --backdrop: #e9e6e2;
    --paper: #ffffff;
    --red: #e3263a;
    --red-deep: #c9142a;
    --ink: #1f1f1f;
    --line-light: rgba(255,255,255,0.85);
  }
  html, body {
    margin: 0;
    padding: 0;
    width: 1200px;
    height: 913px;
    overflow: hidden;
    background: var(--backdrop);
  }
  .canvas {
    position: relative;
    width: 1200px;
    height: 913px;
  }
  .card {
    position: absolute;
    width: 520px;
    height: 297px;
    overflow: hidden;
    box-shadow: 0 10px 28px rgba(0,0,0,0.18);
  }

  /* Front */
  .card-front {
    left: 70px;
    top: 170px;
    background: var(--paper);
  }
  .front-band {
    position: absolute;
    left: 0; right: 0; bottom: 0;
    height: 128px;
    background: linear-gradient(180deg, var(--red) 0%, var(--red-deep) 100%);
  }
  .front-logo {
    position: absolute;
    left: 150px;
    top: 66px;
    display: flex;
    align-items: center;
    gap: 12px;
  }
  .front-logo .mark-dot {
    width: 16px; height: 16px;
    border-radius: 50%;
    background: var(--red);
  }
  .front-logo .wordmark {
    font-family: "Open Sans", sans-serif;
    font-weight: 700;
    font-size: 30px;
    letter-spacing: 1px;
    color: var(--ink);
    text-transform: uppercase;
    line-height: 1;
  }
  .edge-tab {
    position: absolute;
    right: 0;
    top: 150px;
    width: 14px;
    height: 20px;
    background: var(--paper);
  }
  .holder-name {
    position: absolute;
    right: 26px;
    top: 182px;
    font-family: "Libre Baskerville", serif;
    font-size: 15px;
    letter-spacing: 0.5px;
    color: var(--ink);
    text-transform: uppercase;
  }
  .name-rule {
    position: absolute;
    right: 26px;
    top: 206px;
    width: 300px;
    height: 1px;
    background: var(--line-light);
  }
  .contact-rule {
    position: absolute;
    left: 26px;
    top: 226px;
    width: 200px;
    height: 1px;
    background: var(--line-light);
  }
  .contact-list {
    position: absolute;
    left: 26px;
    top: 236px;
    margin: 0;
    padding: 0;
    list-style: none;
    font-family: "Open Sans", sans-serif;
    font-size: 13px;
    color: #fff;
    line-height: 20px;
  }
  .contact-list li {
    display: flex;
    align-items: center;
    gap: 7px;
  }
  .contact-list svg { width: 10px; height: 10px; }

  /* Back */
  .card-back {
    left: 610px;
    top: 446px;
    background: linear-gradient(165deg, #ee4257 0%, var(--red) 40%, var(--red-deep) 100%);
  }
  .back-frame {
    position: absolute;
    left: 78px;
    top: 92px;
    width: 364px;
    height: 112px;
    border: 1px solid var(--line-light);
    box-sizing: border-box;
    display: flex;
    flex-direction: column;
    align-items: center;
    justify-content: center;
    gap: 6px;
  }
  .back-frame .wordmark {
    font-family: "Open Sans", sans-serif;
    font-weight: 700;
    font-size: 32px;
    letter-spacing: 1px;
    color: #fff;
    text-transform: uppercase;
    line-height: 1;
  }
  .back-frame .tagline {
    font-family: "Libre Baskerville", serif;
    font-size: 12px;
    letter-spacing: 1.5px;
    color: #fff;
    text-transform: uppercase;
  }
</style>
</head>
<body>
<main class="canvas">

  <section class="card card-front" aria-label="Card front">
    <div class="front-logo">
      <span class="mark-dot"></span>
      <span class="wordmark">The Pixel Tavern</span>
    </div>
    <div class="front-band"></div>
    <div class="edge-tab"></div>
    <div class="holder-name">Marcus Henley</div>
    <div class="name-rule"></div>
    <div class="contact-rule"></div>
    <ul class="contact-list">
      <li>
        <svg viewBox="0 0 10 10" aria-hidden="true"><path d="M2 0.5 L3.6 2.6 L2.8 3.6 Q4 6 6.4 7.2 L7.4 6.4 L9.5 8 L8.4 9.5 Q3.5 9 0.5 1.6 Z" fill="#fff"/></svg>
        (555) 730-6621
      </li>
      <li>
        <svg viewBox="0 0 10 10" aria-hidden="true"><rect x="0.5" y="1.8" width="9" height="6.4" fill="none" stroke="#fff" stroke-width="1"/><path d="M0.8 2.2 L5 5.4 L9.2 2.2" fill="none" stroke="#fff" stroke-width="1"/></svg>
        kent.w4100@mailbox-demo.net
      </li>
    </ul>
  </section>

  <section class="card card-back" aria-label="Card back">
    <div class="back-frame">
      <span class="wordmark">The Pixel Tavern</span>
      <span class="tagline">Lounge and Arcade</span>
    </div>
  </section>

</main>
</body>
</html>
```